Website for AV installation with booking system and e-commerce

Company: Corvexa
Tag Line: Audio Visual and Security System Installations
We need a website for an AV company based in Sydney Australia. We specialise in Audio Visual, CCTV (security cameras), and Data Cabling.
The purpose of the website is that customers book their installation online with a live booking system.
We are looking for the following:
- Creative and modern design
- easy to use - keep in mind that the user who will book will have little knowledge in technology.
- clean and organised
- colours to work in well with our logo we also like royal to navy blue, but we are open to other suggested what works well with our logo.
We want customers to be able to add products needed for their installation ie when booking to wall mount their TV they can choose to add a TV bracket and cables to the cart and vise-versa buy a bracket or cables and add to cart the installation.
Tabs to be included:
About us
Gallery
Contact Us
Home
Services (there are three services that we offer - Residential, Corporate and Retail)
Products
Book Online/Cart (checkout)
Temporary website checkout: www.corvexa.com.au, please note this is very basic and we do not want a copy of this. This is purely to give you an idea of our company.
Good Luck!
Target Market(s)
home owners/renters, business owners, archiects/designers, builders
Industry/Entity Type
E-Commerce
Look and feel

```html
<!DOCTYPE html>
<html lang="en">
<head>
<meta charset="utf-8">
<title>Corvexa – Audio Visual Security System Installation</title>
<link rel="stylesheet" href="https://fonts.googleapis.com/css2?family=Arimo:wght@400;700&family=Cardo:wght@400&display=swap">
<style>
  :root {
    --sky-top: #b9cde6;
    --sky-mid: #dfe8f3;
    --sky-low: #c3d3e8;
    --panel: #8fc9e7;
    --panel-edge: #5fa8d6;
    --nav: #8ecbe9;
    --divider: #c9e6f5;
    --sheet: #f6f8fa;
    --brand-red: #c8141b;
    --deep-blue: #145f95;
    --navy: #0f3e6e;
    --title-blue: #2a86c2;
    --bullet: #3798cf;
    --ink: #111111;
    --white: #ffffff;
    --search-field: #e9f4fb;
    --search-btn: #8cc8e8;
    --photo-a: #d9cfc4;
    --photo-b: #9a8a7c;
  }
  * { box-sizing: border-box; margin: 0; padding: 0; }
  html, body { width: 1170px; height: 1200px; overflow: hidden; }
  body {
    position: relative;
    font-family: "Arimo", Arial, sans-serif;
    background: linear-gradient(160deg, var(--sky-top) 0%, var(--sky-mid) 35%, var(--sky-low) 70%, var(--sky-mid) 100%);
  }
  .brand {
    position: absolute; left: 40px; top: 62px;
    display: flex; align-items: center; gap: 22px;
    font-weight: 700; font-size: 92px; line-height: 1; color: var(--brand-red);
  }
  .brand-dot { width: 44px; height: 44px; border-radius: 50%; background: var(--brand-red); }
  .address {
    position: absolute; left: 780px; top: 54px;
    font-size: 24px; line-height: 34px; color: var(--ink);
  }
  .search {
    position: absolute; left: 730px; top: 155px; width: 412px; height: 52px;
    display: flex; border-radius: 26px; overflow: hidden;
    box-shadow: 0 2px 8px rgba(15,62,110,.15);
  }
  .search-field {
    flex: 1; background: var(--search-field);
    font-style: italic; color: #9aa8b3; font-size: 24px; padding: 12px 22px;
  }
  .search-btn {
    width: 147px; background: var(--search-btn); color: var(--white);
    font-size: 25px; display: flex; align-items: center; justify-content: center;
  }
  .sheet {
    position: absolute; left: 57px; top: 228px; width: 1050px; height: 490px;
    background: var(--sheet); border-radius: 14px;
    box-shadow: 0 6px 20px rgba(15,62,110,.14);
  }
  .nav {
    position: absolute; left: 57px; top: 228px; width: 1050px; height: 77px;
    background: var(--nav); border-radius: 14px; border: 2px solid var(--white);
    display: flex; align-items: center; justify-content: center;
  }
  .nav-item {
    font-size: 24px; font-weight: 700; color: var(--ink);
    padding: 0 20px; line-height: 48px; white-space: nowrap;
  }
  .nav-item + .nav-item { border-left: 2px solid var(--divider); }
  .nav-item.is-active { color: var(--navy); }
  .hero-photo {
    position: absolute; left: 66px; top: 310px; width: 620px; height: 398px;
    border-radius: 8px;
    background: radial-gradient(ellipse at 45% 45%, var(--photo-a) 0%, #c4b5a6 45%, var(--photo-b) 100%);
  }
  .offers {
    position: absolute; left: 706px; top: 312px; width: 394px; height: 400px;
    background: var(--panel); border-radius: 12px; padding: 40px 0 0 26px;
    font-family: "Cardo", Georgia, serif; color: var(--white);
  }
  .offers h2 { font-weight: 400; font-size: 46px; line-height: 56px; margin-bottom: 38px; }
  .bullet-list { list-style: none; }
  .bullet-list li {
    display: flex; align-items: center; gap: 14px;
    font-size: 41px; line-height: 61px;
  }
  .bullet-list li::before {
    content: ""; width: 30px; height: 26px; background: var(--bullet); flex: none;
  }
  .welcome {
    position: absolute; left: 46px; top: 744px; width: 660px; height: 434px;
    background: var(--panel); border-radius: 12px; border-top: 8px solid var(--panel-edge);
    padding: 22px 0 0 30px; color: var(--white); font-weight: 700;
    box-shadow: 0 6px 20px rgba(15,62,110,.12);
  }
  .welcome h1 { font-size: 42px; line-height: 52px; }
  .welcome h1 .name { font-size: 34px; color: var(--deep-blue); }
  .tagline { font-size: 24px; line-height: 30px; color: var(--ink); margin-bottom: 30px; }
  .welcome p { font-size: 24.5px; line-height: 32px; width: 600px; }
  .welcome p .name { font-size: 32px; color: var(--deep-blue); }
  .welcome p + p { margin-top: 32px; }
  .services {
    position: absolute; left: 735px; top: 747px; width: 371px; height: 431px;
    background: var(--panel); border-radius: 12px; border-top: 8px solid var(--panel-edge);
    padding: 18px 0 0 33px; font-family: "Cardo", Georgia, serif;
    box-shadow: 0 6px 20px rgba(15,62,110,.12);
  }
  .services h2 { font-weight: 400; font-size: 52px; line-height: 60px; color: var(--title-blue); margin-left: 14px; margin-bottom: 30px; }
  .services .bullet-list li { color: var(--white); font-size: 44px; line-height: 72px; gap: 20px; }
</style>
</head>
<body>
  <div class="brand"><span class="brand-dot"></span>Corvexa</div>
  <div class="address">Suite 412, 27 Harlow St,<br>Marrick Junction NSW 2031</div>

  <div class="search">
    <div class="search-field">type here ...</div>
    <div class="search-btn">SEARCH</div>
  </div>

  <div class="sheet"></div>
  <nav class="nav">
    <span class="nav-item is-active">HOME</span>
    <span class="nav-item">About Us</span>
    <span class="nav-item">Services</span>
    <span class="nav-item">Gallery</span>
    <span class="nav-item">Contact Us</span>
    <span class="nav-item">Products</span>
    <span class="nav-item">Book Online</span>
  </nav>

  <div class="hero-photo" role="img" aria-label="Photo of a technician holding a bundle of audio visual cables"></div>

  <section class="offers">
    <h2>Corvexa Offers:</h2>
    <ul class="bullet-list">
      <li>Audio Visual</li>
      <li>CCTV</li>
      <li>Data Cabling</li>
    </ul>
  </section>

  <section class="welcome">
    <h1>Welcome to <span class="name">Corvexa</span></h1>
    <div class="tagline">Audio Visual Security System Installation</div>
    <p><span class="name">Corvexa</span> is based in Sydney providing Professional AV installation services for home &amp; business. We have over 8 years experience in AV equipment and other electronic devices.</p>
    <p>We offer high quality services and can respond quickly to any job.</p>
  </section>

  <section class="services">
    <h2>Our Services</h2>
    <ul class="bullet-list">
      <li>Residential</li>
      <li>Corporate</li>
      <li>Retail</li>
    </ul>
  </section>
</body>
</html>
```